Brightwell PC Help - Web Page
Remote Tech Support Provider
Brightwell PC Help - Web Page -
Creative Brief
24/7 remote PC support. Simple pricing and premium service supporting small business and consumers in the US.
Monthly service plans will be the emphasis but will also provide pay per incident support. Multiple computer discounts will be available and service plans will be structured as follows:
-- $19.99 for upto 3 computers
-- $34.99 for upto 5 computers
-- $79.00 for 10 computers
-- More than 10 computers, call for an instant quote.
KEY OFFERING:
* Automated UNLIMITED Online Backup as an add on for $5/month
Core focus will be on restoring the speed of your computer, removing viruses/malware etc. Will also help users with their WiFi Security Setup, printers, MP3 players, cameras, System Recovery Quillstone Suite, Email and Calendaring Setup, Domain Registration, Web Content Filtering Configuration,
Alternative Software Solution Recommendations... -- ALL for the same monthly fee.
MUST be 100% CSS for me to consider the submission. Prefer clean and simple over cluttered and complex. Every page will have a link that is up front and visible to take you to the order page.
www.vaultmerrow.example
www.helpquorn.example
www.dravelline.example

```html
<!DOCTYPE html>
<html lang="en">
<head>
<meta charset="utf-8">
<title>Brightwell PC Help - Remote Tech Support</title>
<link href="https://fonts.googleapis.com/css2?family=Arimo:wght@400;700&display=swap" rel="stylesheet">
<style>
:root{
  --green:#8cb63c;
  --green-dark:#6e9a1f;
  --green-pale:#eef3dd;
  --green-line:#c9dc9c;
  --nav-dark:#2e3336;
  --nav-mid:#4a5155;
  --text:#333;
  --muted:#666;
  --link:#5c8a12;
  --orange:#f0a21e;
  --footer:#e6ecd2;
}
*{box-sizing:border-box;margin:0;padding:0}
html,body{width:1200px;height:901px;overflow:hidden;background:#fff}
body{font-family:"Arimo",Arial,sans-serif;color:var(--text);font-size:11px;position:relative}
a{color:var(--link)}
.header{position:absolute;left:165px;top:0;width:920px;height:92px}
.brand{position:absolute;left:10px;top:18px;display:flex;align-items:center;gap:10px;font-size:26px;font-weight:700;color:var(--green-dark)}
.brand-mark{width:34px;height:34px;border-radius:50%;background:var(--green)}
.service{position:absolute;right:30px;top:14px;text-align:left}
.service small{display:block;font-size:11px;color:var(--text)}
.phone{display:flex;align-items:center;gap:8px;font-size:26px;color:#111;margin-top:4px}
.nav{position:absolute;left:162px;top:95px;width:926px;height:26px;background:linear-gradient(var(--nav-mid),var(--nav-dark));display:flex;padding-left:10px}
.nav a{color:#fff;text-decoration:none;font-size:11px;line-height:26px;padding:0 18px;border-right:1px solid #555}
.nav a.active{background:linear-gradient(#a9cf55,var(--green))}
.main{position:absolute;left:175px;top:132px;width:675px}
.hero{height:318px;background:linear-gradient(135deg,#e9e4dc 0%,#b8b0a4 35%,#3a3f47 70%,#1e2228 100%);position:relative}
.hero-band{position:absolute;left:0;top:16px;width:100%;height:42px;background:rgba(30,34,40,.75);color:#fff;font-size:20px;font-weight:700;text-align:right;padding-right:12px;line-height:42px}
.hero-band em{font-style:normal;color:var(--orange)}
h1,h2{color:var(--green-dark);font-size:20px;font-weight:700}
h1{margin-top:12px}
.intro{margin-top:5px;line-height:1.35;font-size:11px}
.features{display:flex;justify-content:space-between;margin-top:14px}
.feature{width:205px;text-align:center}
.pill{display:block;background:linear-gradient(#a9cf55,var(--green-dark));color:#1b2a06;font-weight:700;border-radius:4px;height:22px;line-height:22px;font-size:11px}
.feature .art{display:flex;gap:8px;margin-top:10px;text-align:justify;align-items:flex-start}
.icon{flex:0 0 52px;height:52px;border-radius:50%;background:radial-gradient(circle at 35% 35%,#9fd0e8,#2e6f9c)}
.feature p{line-height:1.3}
h2{margin-top:32px}
.solutions{margin-top:6px;line-height:1.35}
.join{display:inline-block;background:linear-gradient(#f7c65c,var(--orange));border:1px solid #c77f10;color:#4a2a00;border-radius:5px;font-size:11px;font-weight:700;padding:4px 12px;margin-top:8px;text-decoration:none}
.sidebar{position:absolute;left:862px;top:132px;width:218px}
.box{background:var(--green-pale);border:1px solid var(--green-line);margin-bottom:12px}
.box h3{font-size:11px;font-weight:700;background:linear-gradient(#d7e6b0,#c3d98c);height:26px;line-height:26px;padding-left:10px;display:flex;align-items:center;gap:6px}
.box h3::before{content:"";width:10px;height:10px;border-radius:50%;background:var(--green-dark)}
.box-body{padding:8px 10px;line-height:1.35}
.box label{display:block;margin-top:4px}
.box input{display:block;width:100%;height:16px;border:1px solid #b8c79a;margin-top:2px;background:#fff}
.plans{list-style:none;margin-top:3px}
.plans li{font-weight:700;padding-left:10px;position:relative}
.plans li::before{content:"";position:absolute;left:0;top:4px;width:5px;height:5px;background:var(--green-dark)}
.footer{position:absolute;left:162px;top:878px;width:926px;height:23px;background:var(--footer);text-align:center;font-size:9px;line-height:10px;padding-top:2px}
.rss{position:absolute;left:10px;top:4px;width:14px;height:14px;border-radius:3px;background:var(--orange)}
</style>
</head>
<body>
<header class="header">
  <div class="brand"><span class="brand-mark"></span>Brightwell PC Help</div>
  <div class="service">
    <small>Brightwell PC Help Customer Service</small>
    <div class="phone">
      <svg width="22" height="20" viewBox="0 0 22 20"><path d="M2 6c0-3 4-4 9-4s9 1 9 4v2h-5V6H7v2H2z" fill="#111"/><rect x="4" y="9" width="14" height="10" rx="2" fill="#111"/></svg>
      1-555-014-2277
    </div>
  </div>
</header>
<nav class="nav">
  <a class="active" href="#">Home</a><a href="#">About</a><a href="#">Services</a><a href="#">Support</a><a href="#">Contact</a>
</nav>
<main class="main">
  <div class="hero" role="img" aria-label="Photo of a hand typing on a laptop keyboard">
    <div class="hero-band">Automated UNLIMITED Offline Backup as an add on for <em>$5/month</em></div>
  </div>
  <h1>Remote Tech Support Provider</h1>
  <p class="intro">Lorem ipsum dolor sit amet, <a href="#">link</a>, <a href="#">visited link</a>, <a href="#" style="color:var(--orange)">hover state</a> consectetuer adipiscing elit. Quisque sed felis. Aliquam sit amet felis. Mauris semper, velit semper laoreet dictum, quam diam dictum urna, nec placerat elit nisl in quam. Etiam augue pede, molestie eget, rhoncus at, convallis ut, eros.</p>
  <div class="features">
    <div class="feature"><span class="pill">Technical Support</span>
      <div class="art"><span class="icon" role="img" aria-label="Support headset icon"></span><p>24/7 remote PC support. Simple pricing and premium service supporting small business and consumers in the US.</p></div></div>
    <div class="feature"><span class="pill">Speed Up Your Computer</span>
      <div class="art"><span class="icon" role="img" aria-label="Speed gauge icon"></span><p>Lorem ipsum dolor sit amet, consectetuer adipiscing elit. Quisque sed felis. Aliquam sit amet felis. Mauris semper, velit semper laoreet dictum, quam diam dictum urna.</p></div></div>
    <div class="feature"><span class="pill">Removing Viruses</span>
      <div class="art"><span class="icon" role="img" aria-label="Virus shield icon"></span><p>Lorem ipsum dolor sit amet, consectetuer adipiscing elit. Quisque sed felis. Aliquam sit amet felis. Mauris semper, velit semper laoreet dictum, quam diam dictum urna.</p></div></div>
  </div>
  <h2>Solutions</h2>
  <p class="solutions">Lorem ipsum dolor sit amet, consectetuer adipiscing elit, <a href="#">text link</a>. Nullam dignissim convallis est. Quisque aliquam. Nunc iaculis suscipit dui. Nam sit amet sem. Aliquam libero nisi, imperdiet at, tincidunt nec, gravida vehicula, nisl. Praesent mattis, massa quis luctus fermentum, turpis mi volutpat justo, eu volutpat enim diam eget metus. Maecenas ornare tortor.</p>
  <a class="join" href="#">Join Now</a>
</main>
<aside class="sidebar">
  <section class="box"><h3>Start Your Free Trial</h3>
    <form class="box-body">
      <label>Email Address<input type="text"></label>
      <label>Password<input type="password"></label>
      <label>Confirm Password<input type="password"></label>
      <a class="join" href="#">Join Now</a>
    </form>
  </section>
  <section class="box"><h3>Monthly Service Plans</h3>
    <div class="box-body">
      <p>Monthly service plans will be the emphasis but will also provide pay per incident support. Multiple computer discounts will be available and service plans will be structured as follows:</p>
      <ul class="plans">
        <li>$19.99 for upto 3 computers</li>
        <li>$34.99 for upto 5 computers</li>
        <li>$79.00 for 10 computers</li>
        <li>More than 10 computers, call for an instant quote.</li>
      </ul>
      <a href="#" style="font-weight:700">Read more...</a>
    </div>
  </section>
  <section class="box"><h3>Contact Info</h3>
    <div class="box-body">
      <p><b>Brightwell PC Help</b><br>US, 12345<br>Email: <a href="#">info@brightwellpchelp.example</a></p>
      <p style="margin-top:6px">Phone: (555) 014-7890<br>Fax: (555) 014-7899</p>
    </div>
  </section>
</aside>
<footer class="footer">
  <span class="rss"></span>
  <a href="#">Contact Us</a> | <a href="#">Terms of Use</a> | <a href="#">Privacy Statement</a><br>
  Copyright © 2011 Brightwell PC Help. All Rights Reserved.
</footer>
</body>
</html>
```